Unique Elegant Stationary Set

Prepare a unique eye catching stationary set consisting of :
(1) Letterhead
(2) A3 Envelope
(3) Business Card
(4) Email Signature Banner

Package to be elegant, modern, and designers not only to think of design or colors but also materials could make a big difference, embossing, debossing, glossy, matt ....etc.

I attached both our new logos (Stacked or Linear) noting you may use any of them but you cant modify anything in the logos. Also attached our final draft portfolio to see what type of projects we work on and i also have here a glimboard page link showing the direction we want: https://www.glimboard.example/ravelkoton/business-card-design/

Target Market(s)

VVIP / Elite Developers

Industry/Entity Type

Architecture

Font styles to use
Sans Serif
Other font styles liked:
• unitext

Requirements
Should not have
• too many colors, or being busy in general. We want something pleasing to the eye

```html
<!DOCTYPE html>
<html lang="en">
<head>
<meta charset="utf-8">
<title>Vora Design Stationery Set</title>
<link rel="stylesheet" href="https://fonts.googleapis.com/css2?family=Roboto:wght@300;400;500;700&display=swap">
<style>
:root{
  --brand-red:#c41e24;
  --backdrop:#3b3b3d;
  --paper:#f5f2f2;
  --white:#ffffff;
  --ink:#4a4a4a;
  --ink-soft:#6b6b6b;
  --footer-grey:#6e6e6e;
}
*{box-sizing:border-box;margin:0;padding:0}
html,body{width:1200px;height:624px;overflow:hidden}
body{background:var(--backdrop);font-family:"Roboto",Arial,sans-serif;color:var(--ink);position:relative}
.piece{position:absolute;overflow:hidden;box-shadow:0 2px 6px rgba(0,0,0,.35)}
.wordmark{font-family:"Roboto",Arial,sans-serif;font-weight:700;color:var(--white);white-space:nowrap;letter-spacing:.5px}
.icon{width:5px;height:5px;display:inline-block;vertical-align:middle;margin-right:3px}
.icon path,.icon circle,.icon rect{fill:var(--brand-red)}
.on-red .icon path,.on-red .icon rect{fill:var(--white)}

/* business card front */
.card-front{left:46px;top:125px;width:268px;height:153px;background:var(--white)}
.card-front .stacked-mark{position:absolute;left:44px;top:58px;width:100px;text-align:center;color:var(--brand-red);font-weight:700}
.stacked-mark .mark-main{font-size:27px;line-height:27px;letter-spacing:1px}
.stacked-mark .mark-sub{font-size:7.5px;letter-spacing:6px;margin-top:3px;padding-left:6px}
.card-front .divider{position:absolute;left:140px;top:36px;width:1px;height:80px;background:#cfcfcf}
.card-front .details{position:absolute;left:149px;top:38px;font-size:6px;line-height:8px;color:var(--ink)}
.details .name{font-size:10px;font-weight:700;color:var(--brand-red);line-height:11px;letter-spacing:.3px}
.details .role{color:#8a8a8a;margin-bottom:7px}
.details .address{margin-bottom:4px}

/* business card back */
.card-back{left:41px;top:336px;width:273px;height:156px;background:var(--brand-red)}
.card-back .wordmark{position:absolute;left:52px;top:62px;font-size:28px}

/* letterhead */
.letterhead{left:342px;top:54px;width:375px;height:528px;background:var(--paper)}
.letterhead .header{position:absolute;left:0;top:0;width:100%;height:58px;background:var(--brand-red)}
.letterhead .header .wordmark{position:absolute;left:38px;top:19px;font-size:19px}
.letterhead .header .contact{position:absolute;left:261px;top:14px;font-size:5.6px;line-height:7.6px;color:var(--white)}
.letterhead .body{position:absolute;left:38px;top:128px;width:302px}
.letterhead .salutation{font-size:10px;color:var(--ink);margin-bottom:16px}
.letterhead p{font-size:5.4px;line-height:9px;color:var(--ink-soft);text-align:justify;margin-bottom:9px}
.letterhead .closing{font-size:5.8px;color:var(--ink-soft);margin-top:12px}
.letterhead .signature{display:block;width:50px;height:22px;margin:6px 0 4px -2px;background:linear-gradient(90deg,rgba(40,40,40,.05),rgba(40,40,40,.22),rgba(40,40,40,.05));border-radius:3px}
.letterhead .signer{font-size:8px;color:var(--ink);margin-left:2px}
.letterhead .signer-role{font-size:6px;color:var(--ink-soft);margin-left:2px;margin-top:2px}
.letterhead .footer{position:absolute;left:0;bottom:0;width:100%;height:12px;background:var(--footer-grey);color:var(--white);font-size:5.6px;line-height:12px;text-align:center}

/* long envelope */
.envelope-long{left:774px;top:65px;width:381px;height:104px;background:var(--paper)}
.envelope-long .header{position:absolute;left:0;top:0;width:100%;height:39px;background:var(--brand-red)}
.envelope-long .wordmark{position:absolute;left:25px;top:11px;font-size:18px}
.envelope-long .header .contact{position:absolute;right:22px;top:14px;font-size:5.6px;line-height:7.6px;color:var(--white);text-align:right}
.envelope-long .contact-list{position:absolute;right:26px;top:56px;font-size:5.6px;line-height:7.6px;text-align:right;color:var(--ink)}
.contact-list .icon{margin:0 0 0 3px}
.envelope-long .strip{position:absolute;left:0;bottom:0;width:100%;height:8px;background:var(--footer-grey)}

/* envelope back with flap */
.envelope-flap{left:784px;top:198px;width:349px;height:246px;background:var(--paper);box-shadow:none}
.envelope-flap svg.flap{position:absolute;left:0;top:0}
.envelope-flap .stacked-mark{position:absolute;left:140px;top:15px;width:70px;text-align:center;color:var(--white);font-weight:700}
.envelope-flap .mark-main{font-size:19px;line-height:19px}
.envelope-flap .mark-sub{font-size:5.5px;letter-spacing:4.5px;margin-top:2px;padding-left:4px}

/* envelope front */
.envelope-front{left:745px;top:323px;width:348px;height:246px;background:var(--paper)}
.envelope-front .header{position:absolute;left:0;top:0;width:100%;height:58px;background:var(--brand-red)}
.envelope-front .wordmark{position:absolute;left:25px;top:20px;font-size:18px}
.envelope-front .return-address{position:absolute;left:25px;top:192px;font-size:5.8px;line-height:7.6px;color:var(--ink)}
.envelope-front .return-address .lines{margin-bottom:4px}
.envelope-front .footer{position:absolute;left:0;bottom:0;width:100%;height:11px;background:var(--footer-grey);color:var(--white);font-size:5.6px;line-height:11px;padding-left:25px}
</style>
</head>
<body>

<section class="piece card-front" aria-label="Business card, front">
  <div class="stacked-mark"><div class="mark-main">VORA</div><div class="mark-sub">DESIGN</div></div>
  <div class="divider"></div>
  <div class="details">
    <div class="name">ADRIAN VALE</div>
    <div class="role">President</div>
    <div class="address">214 Larchmere Court<br>Halden, Canada 20418</div>
    <div><svg class="icon" viewBox="0 0 10 10"><path d="M2 0l2 2-1 2 3 3 2-1 2 2-2 2C4 10 0 6 0 2z"/></svg>555-210-4471</div>
    <div><svg class="icon" viewBox="0 0 10 10"><rect x="2" y="0" width="6" height="10" rx="1"/></svg>555-210-4479</div>
    <div><svg class="icon" viewBox="0 0 10 10"><path d="M0 2h10v6H0z"/></svg>info@voradesign.example</div>
    <div><svg class="icon" viewBox="0 0 10 10"><circle cx="5" cy="5" r="5"/></svg>www.voradesign.example</div>
  </div>
</section>

<section class="piece card-back" aria-label="Business card, back">
  <div class="wordmark">VORA DESIGN</div>
</section>

<section class="piece letterhead" aria-label="Letterhead">
  <header class="header on-red">
    <div class="wordmark">VORA DESIGN</div>
    <div class="contact">
      214 Larchmere Court<br>Halden, Canada 20418<br>
      <svg class="icon" viewBox="0 0 10 10"><path d="M2 0l2 2-1 2 3 3 2-1 2 2-2 2C4 10 0 6 0 2z"/></svg>5552104400<br>
      <svg class="icon" viewBox="0 0 10 10"><path d="M0 2h10v6H0z"/></svg>studio@voradesign.example
    </div>
  </header>
  <div class="body">
    <div class="salutation">Dear Mr. Vale,</div>
    <p>Lorem ipsum dolor sit amet, consectetur adipiscing elit. Donec orci purus, luctus vitae dignissim eu, iaculis sed purus. Vivamus faucibus, ipsum nec aliquet viverra, leo mauris condimentum ligula, sit amet sagittis enim ligula quis arcu. Nam egestas tortor id nisi porttitor mattis. In tortor ante, ultricies in suscipit a, tempus non massa. Vivamus et auctor mi. Fusce vel massa nulla. Phasellus nec eros mauris, et scelerisque orci.</p>
    <p>Donec malesuada orci vitae nulla accumsan porta a id massa. Quisque accumsan iaculis magna sit amet fringilla. Maecenas consequat, magna eget tincidunt semper, odio nibh rutrum mi, id feugiat ante nisi eu risus. Vestibulum nunc orci, rhoncus a placerat in, ultricies in mi. Cras mattis varius eros, vel fringilla nisi suscipit eget. Quisque scelerisque sagittis nulla at porttitor.</p>
    <p>Sed id augue vitae urna euismod commodo aliquet a quam. Pellentesque arcu velit, cursus et malesuada ut, consequat et diam. Nullam erat sem, rhoncus id ullamcorper vitae, rhoncus et arcu. In ultricies ultricies nulla, ut rutrum nisi iaculis at. Donec eu magna a metus ornare faucibus. Fusce aliquet faucibus ultricies. Morbi semper, est id tincidunt gravida, sem arcu adipiscing lacus, ac bibendum nulla leo eu purus. Quisque nec diam sed risus consectetur a cumsan quis quis nibh. Vestibulum id purus lorem.</p>
    <p>It is a long established fact that a reader will be distracted by the readable content of a page when looking at its layout. The point of using Lorem Ipsum is that it has a more-or-less normal distribution of letters, as opposed to using 'Content here, content here', making it look like readable English. Many desktop publishing packages</p>
    <div class="closing">Sincerely,</div>
    <span class="signature" role="img" aria-label="Handwritten signature"></span>
    <div class="signer">Adrian Vale</div>
    <div class="signer-role">CEO/ Founder</div>
  </div>
  <footer class="footer">www.voradesign.example</footer>
</section>

<section class="piece envelope-long" aria-label="Long envelope">
  <header class="header on-red">
    <div class="wordmark">VORA DESIGN</div>
    <div class="contact">214 Larchmere Court<br>Halden, Canada 20418</div>
  </header>
  <div class="contact-list">
    <div>555-210-4471<svg class="icon" viewBox="0 0 10 10"><path d="M2 0l2 2-1 2 3 3 2-1 2 2-2 2C4 10 0 6 0 2z"/></svg></div>
    <div>info@voradesign.example<svg class="icon" viewBox="0 0 10 10"><path d="M0 2h10v6H0z"/></svg></div>
    <div>www.voradesign.example<svg class="icon" viewBox="0 0 10 10"><circle cx="5" cy="5" r="5"/></svg></div>
  </div>
  <div class="strip"></div>
</section>

<section class="piece envelope-flap" aria-label="Envelope, back with flap">
  <svg class="flap" width="349" height="60" viewBox="0 0 349 60"><path d="M0 0H349L343 30Q340 58 312 58H37Q9 58 6 30Z" fill="var(--brand-red)"/></svg>
  <div class="stacked-mark"><div class="mark-main">VORA</div><div class="mark-sub">DESIGN</div></div>
</section>

<section class="piece envelope-front" aria-label="Envelope, front">
  <header class="header"><div class="wordmark">VORA DESIGN</div></header>
  <div class="return-address">
    <div class="lines">214 Larchmere Court<br>Halden, Canada 20418</div>
    <div><svg class="icon" viewBox="0 0 10 10"><path d="M2 0l2 2-1 2 3 3 2-1 2 2-2 2C4 10 0 6 0 2z"/></svg>555-210-4471</div>
    <div><svg class="icon" viewBox="0 0 10 10"><path d="M0 2h10v6H0z"/></svg>info@voradesign.example</div>
  </div>
  <footer class="footer">www.voradesign.example</footer>
</section>

</body>
</html>
```